Stationary for a manufacturing company
Velmoré Professional Wear
Creative Brief
Simple
John Doe
VP Sales and Marketing
123 Street Name, City Country Zip Code
example@email.com
www.example.com
Font: Hug me Tight and Neuropol Velmoré is a brand that creates professional uniforms- chefs, corporate, and etc Business card and stationary designs are up to the designers. My only comments are to make the business card: 1.) Easy to read 2.) Professional looking 3.) Clean I have uploaded photos of the logo and the shade of red used Logo should also appear in the front of the card. Also, no need to limit yourself in using the same font as the logo. Feel free to use other fonts
Use logo uploaded (side icon, red background). Red Background. Shade of red will be provided in the uploads.
sodrk sodrk
Designers Please add the company name on top of the address or wherever you think it will fit. For now, please use "Example Company, Inc."

```html
<!DOCTYPE html>
<html lang="en">
<head>
<meta charset="utf-8">
<title>Velmoré Professional Wear – Business Card</title>
<link rel="stylesheet" href="https://fonts.googleapis.com/css2?family=Exo+2:wght@300;400;600&family=Arimo&display=swap">
<style>
  :root {
    --stage: #000000;
    --brand-red: #ad1500;
    --paper: #ffffff;
    --label: #ffffff;
    --text-dark: #4a4a4a;
  }
  * { margin: 0; padding: 0; box-sizing: border-box; }
  html, body {
    width: 1200px;
    height: 830px;
    overflow: hidden;
    background: var(--stage);
  }
  .canvas {
    position: relative;
    width: 1200px;
    height: 830px;
    background: var(--stage);
    font-family: "Exo 2", sans-serif;
  }
  .card {
    position: absolute;
    top: 250px;
    width: 475px;
    height: 262px;
    overflow: hidden;
  }
  .card--front { left: 125px; background: var(--paper); }
  .card--back  { left: 622px; background: var(--brand-red); }

  .front-band {
    position: absolute;
    left: 0; top: 0;
    width: 190px;
    height: 100%;
    background: var(--brand-red);
  }
  .holder-name {
    position: absolute;
    left: 271px;
    top: 58px;
    font-size: 27px;
    font-weight: 400;
    color: var(--brand-red);
    letter-spacing: 0.5px;
  }
  .holder-title {
    position: absolute;
    left: 292px;
    top: 97px;
    font-size: 9px;
    font-weight: 300;
    color: var(--brand-red);
  }
  .contact-list {
    position: absolute;
    left: 286px;
    top: 134px;
    list-style: none;
  }
  .contact-list li {
    display: flex;
    align-items: center;
    height: 17px;
    font-size: 8px;
    color: var(--brand-red);
  }
  .contact-list .dot {
    width: 7px; height: 7px;
    margin-right: 7px;
    border: 1.5px solid var(--brand-red);
    border-radius: 50%;
  }

  .brand-lockup {
    position: absolute;
    left: 0; right: 0;
    top: 112px;
    display: flex;
    justify-content: center;
    align-items: center;
    gap: 6px;
  }
  .brand-mark {
    width: 16px; height: 16px;
    border-radius: 50%;
    background: var(--paper);
  }
  .brand-name {
    font-size: 24px;
    font-weight: 600;
    color: var(--paper);
  }
  .brand-web {
    position: absolute;
    left: 0; right: 0;
    top: 150px;
    text-align: center;
    font-size: 7px;
    color: var(--paper);
  }

  .side-label {
    position: absolute;
    top: 540px;
    width: 200px;
    text-align: center;
    font-family: "Arimo", sans-serif;
    font-size: 26px;
    color: var(--label);
  }
  .side-label--front { left: 267px; }
  .side-label--back  { left: 807px; }
</style>
</head>
<body>
<main class="canvas">
  <section class="card card--front">
    <div class="front-band"></div>
    <h1 class="holder-name">John Doe</h1>
    <p class="holder-title">VP Sales and Marketing</p>
    <ul class="contact-list">
      <li><span class="dot"></span>123 Street Name City Country 1234</li>
      <li><span class="dot"></span>+00 123 456 789</li>
      <li><span class="dot"></span>+00 987 654 321</li>
      <li><span class="dot"></span>www.example.com</li>
      <li><span class="dot"></span>example@email.com</li>
    </ul>
  </section>

  <section class="card card--back">
    <div class="brand-lockup">
      <span class="brand-mark"></span>
      <span class="brand-name">Velmoré</span>
    </div>
    <p class="brand-web">www.example.com</p>
  </section>

  <p class="side-label side-label--front">font</p>
  <p class="side-label side-label--back">back</p>
</main>
</body>
</html>
```